Crestwell Renewal Business Card Design Phase 2

Professional and clean design. The design colors should flow with the logo. Two-sided card with the website on the back which is:

www.CrestwellRenewal.example.

"Specializing in Water Damage Restoration"

On the front I need the name, email, phone, and logo.

Name: Dorian Halvek
Email: Dorian@CrestwellRenewal.example
Phone: 555-318-2046 for now

I only have the Preview and Thumbnail right now but should have the source files uploaded within a day or two.

Target Market(s)

Flood victims, home owners with water damage from busted pipes etc...

Industry/Entity Type

Business

Contact Information for Business Card

Name: Dorian Halvek

Font styles to use
Serif
Sans Serif

Requirements
Must have
• Business Card Details Info

```html
<!DOCTYPE html>
<html lang="en">
<head>
<meta charset="utf-8">
<title>Crestwell Renewal Business Card</title>
<link href="https://fonts.googleapis.com/css2?family=Oswald:wght@600&family=Open+Sans:wght@400;600&family=Cormorant+Garamond:wght@600&display=swap" rel="stylesheet">
<style>
:root{
  --navy:#1d3563;
  --green:#3f8f35;
  --paper:#ffffff;
  --bg:#e9ebee;
  --ghost:#dfe3e8;
  --ghost-green:#e3ebe2;
  --ink:#2a3550;
}
*{margin:0;padding:0;box-sizing:border-box}
html,body{width:1200px;height:900px;overflow:hidden;background:var(--bg)}
.canvas{position:relative;width:1200px;height:900px}
.card{position:absolute;left:250px;width:700px;height:400px;background:var(--paper);border-radius:22px;overflow:hidden;box-shadow:0 6px 18px rgba(0,0,0,.12)}
.card--back{top:35px}
.card--front{top:465px}
.card__deco{position:absolute;inset:0;width:700px;height:400px}
.wordmark{position:absolute;font-family:"Oswald",sans-serif;font-weight:600;color:var(--navy);line-height:.95;letter-spacing:1px;text-transform:uppercase;white-space:nowrap}
.wordmark__dot{display:inline-block;width:.32em;height:.32em;border-radius:50%;background:var(--green);margin-left:.12em;vertical-align:middle}
.card--back .wordmark{left:150px;top:85px;font-size:70px}
.tagline{position:absolute;right:62px;top:258px;font-family:"Cormorant Garamond",serif;font-weight:600;font-size:15px;letter-spacing:2px;color:var(--navy);text-transform:uppercase;white-space:nowrap;line-height:1}
.website{position:absolute;right:62px;top:284px;font-family:"Open Sans",sans-serif;font-size:17px;color:var(--navy);white-space:nowrap;line-height:1.2}
.card--front .wordmark{left:38px;top:48px;font-size:50px}
.illustration{position:absolute;left:230px;top:20px;width:380px;height:250px;border-radius:12px;background:linear-gradient(160deg,var(--ghost-green) 0%,var(--ghost) 60%,rgba(223,227,232,.4) 100%);opacity:.8}
.person-name{position:absolute;right:62px;top:178px;font-family:"Oswald",sans-serif;font-weight:600;font-size:27px;letter-spacing:1px;text-transform:uppercase;white-space:nowrap}
.person-name__first{color:var(--green)}
.person-name__last{color:var(--navy)}
.contacts{position:absolute;left:44px;top:300px;list-style:none;font-family:"Open Sans",sans-serif;font-size:16px;color:var(--ink);white-space:nowrap}
.contacts li{display:flex;align-items:center;gap:10px;height:24px}
.contacts svg{width:13px;height:13px;fill:var(--green)}
</style>
</head>
<body>
<div class="canvas">

  <section class="card card--back">
    <svg class="card__deco" viewBox="0 0 700 400" aria-hidden="true">
      <polygon points="0,400 0,368 212,368 246,334 272,334 236,400" fill="var(--navy)"/>
      <rect x="272" y="334" width="428" height="6" fill="var(--green)"/>
    </svg>
    <div class="wordmark">Crestwell<br>Renewal<span class="wordmark__dot"></span></div>
    <p class="tagline">Specializing in Water Damage Restoration</p>
    <p class="website">www.CrestwellRenewal.example</p>
  </section>

  <section class="card card--front">
    <div class="illustration" role="img" aria-label="Faint illustration of a house and a technician with a water extraction hose"></div>
    <svg class="card__deco" viewBox="0 0 700 400" aria-hidden="true">
      <rect x="430" y="222" width="210" height="4" fill="var(--navy)"/>
      <polygon points="628,238 700,238 700,282 612,282" fill="var(--navy)"/>
      <rect x="40" y="283" width="575" height="3" fill="var(--green)"/>
      <polygon points="300,400 700,400 700,376 330,376" fill="var(--green)"/>
    </svg>
    <div class="wordmark">Crestwell<br>Renewal<span class="wordmark__dot"></span></div>
    <p class="person-name"><span class="person-name__first">Dorian</span> <span class="person-name__last">Halvek</span></p>
    <ul class="contacts">
      <li><svg viewBox="0 0 24 24"><path d="M6.6 10.8a15.1 15.1 0 0 0 6.6 6.6l2.2-2.2c.3-.3.7-.4 1-.2 1.1.4 2.3.6 3.6.6.6 0 1 .4 1 1V20c0 .6-.4 1-1 1A17 17 0 0 1 3 4c0-.6.4-1 1-1h3.5c.6 0 1 .4 1 1 0 1.3.2 2.5.6 3.6.1.3 0 .7-.2 1z"/></svg>555-318-2046</li>
      <li><svg viewBox="0 0 24 24"><path d="M2 5h20v14H2zm2 2v.5l8 5 8-5V7zm0 2.9V17h16V9.9l-8 5z"/></svg>Dorian@CrestwellRenewal.example</li>
      <li><svg viewBox="0 0 24 24"><path d="M12 2a10 10 0 1 0 0 20 10 10 0 0 0 0-20zm6.9 9h-3a15 15 0 0 0-1.3-5.6A8 8 0 0 1 18.9 11zM12 4c.9 1.2 1.8 3.7 1.9 7h-3.8c.1-3.3 1-5.8 1.9-7zM9.4 5.4A15 15 0 0 0 8.1 11h-3a8 8 0 0 1 4.3-5.6zM5.1 13h3a15 15 0 0 0 1.3 5.6A8 8 0 0 1 5.1 13zM12 20c-.9-1.2-1.8-3.7-1.9-7h3.8c-.1 3.3-1 5.8-1.9 7zm2.6-1.4a15 15 0 0 0 1.3-5.6h3a8 8 0 0 1-4.3 5.6z"/></svg>www.CrestwellRenewal.example</li>
    </ul>
  </section>

</div>
</body>
</html>
```